Ferncrest Builders Reclad information brochure

We require a brochure/info booklet front cover designed for a lead magnet - it will be called "the 5 things you need to know before recladding your home"

Should include lifestyle image to connect with potential customer (maybe a family on a computer) the title should be relatively large/readable as it will be scaled down on our website as a download/lead magnet and also used on landing pages and social media. our company colours are black/white/grey but these do no need to be used, whatever makes the cover more visually appealing - our logo should be used somewhere on the cover but can be small.

we require a PDF copy to use as the cover and also a 3d render standing up for the advertising/magnet.

```html
<!DOCTYPE html>
<html lang="en">
<head>
<meta charset="utf-8">
<title>The 5 Things You Need to Know Before Recladding Your Home</title>
<link rel="stylesheet" href="https://fonts.googleapis.com/css2?family=Montserrat:wght@600;800&display=swap">
<style>
  :root {
    --navy: #1e3350;
    --sky: #4a8fd0;
    --paper: #ffffff;
    --photo-light: #f1efec;
    --photo-mid: #d8c6bb;
    --photo-warm: #c9a08a;
    --photo-shade: #6f5a52;
  }
  html, body {
    margin: 0;
    padding: 0;
    overflow: hidden;
    background: var(--paper);
  }
  .cover {
    position: relative;
    width: 841px;
    height: 1200px;
    background: var(--paper);
    overflow: hidden;
    font-family: "Montserrat", sans-serif;
  }
  .cover-title {
    position: absolute;
    top: 66px;
    left: 0;
    width: 100%;
    margin: 0;
    text-align: center;
    text-transform: uppercase;
    line-height: 1;
  }
  .title-line {
    display: block;
  }
  .title-lead {
    font-weight: 800;
    font-size: 100px;
    letter-spacing: -1px;
    color: var(--navy);
  }
  .title-sub {
    margin-top: 16px;
    font-weight: 600;
    font-size: 35px;
    letter-spacing: 0.5px;
    color: var(--navy);
  }
  .title-key {
    margin-top: 14px;
    font-weight: 800;
    font-size: 100px;
    letter-spacing: -1px;
    color: var(--sky);
  }
  .title-end {
    margin-top: 10px;
    font-weight: 800;
    font-size: 104px;
    letter-spacing: -1px;
    color: var(--navy);
  }
  .lifestyle-photo {
    position: absolute;
    left: 0;
    top: 532px;
    width: 841px;
    height: 668px;
    background:
      radial-gradient(ellipse 55% 40% at 50% 35%, var(--photo-warm) 0%, rgba(201,160,138,0) 70%),
      linear-gradient(180deg, var(--photo-light) 0%, var(--photo-mid) 50%, #a8908a 80%, var(--photo-shade) 100%);
  }
  .brand {
    position: absolute;
    left: 90px;
    bottom: 44px;
    display: flex;
    align-items: center;
    gap: 10px;
    font-family: "Montserrat", sans-serif;
    font-weight: 800;
    font-size: 24px;
    letter-spacing: 1px;
    text-transform: uppercase;
    color: var(--paper);
  }
  .brand-dot {
    width: 30px;
    height: 30px;
    border-radius: 50%;
    background: var(--paper);
  }
</style>
</head>
<body>
  <main class="cover">
    <h1 class="cover-title">
      <span class="title-line title-lead">The 5 Things</span>
      <span class="title-line title-sub">You need to know before</span>
      <span class="title-line title-key">Recladding</span>
      <span class="title-line title-end">Your Home</span>
    </h1>
    <div class="lifestyle-photo" role="img" aria-label="Photo of a smiling family of four gathered on a white sofa looking at a laptop together in a bright living room"></div>
    <div class="brand">
      <span class="brand-dot"></span>
      <span class="brand-name">Ferncrest Builders</span>
    </div>
  </main>
</body>
</html>
```